Software allocation system needs a business card design

We need a business card designed for our software platform - www.tolvexa.com.au

At the moment the logo and website is all black and white, we are happy for suggestions on implementing some colour throughout either the logo or business card.

Industry/Entity Type

Software

Font styles to use
Sans Serif

Colors

Designer to choose colors to be used in the design.

```html
<!DOCTYPE html>
<html lang="en">
<head>
<meta charset="utf-8">
<title>Tolvexa business card</title>
<link rel="stylesheet" href="https://fonts.googleapis.com/css2?family=Montserrat:wght@300;400&display=swap">
<style>
  :root {
    --backdrop: #d9dbd9;
    --card-dark: #2a2123;
    --card-dark-edge: #1c1618;
    --card-light: #ffffff;
    --accent: #e0402b;
    --logo-grey: #b9b9b9;
    --text-grey: #9a9a9a;
    --text-mid: #8c8c8c;
  }
  * { margin: 0; padding: 0; box-sizing: border-box; }
  html, body { width: 1200px; height: 900px; overflow: hidden; }
  body {
    background: var(--backdrop);
    font-family: "Montserrat", Arial, sans-serif;
    position: relative;
  }
  .card {
    position: absolute;
    left: 330px;
    width: 540px;
    height: 309px;
    box-shadow: 0 6px 18px rgba(0,0,0,0.18);
    overflow: hidden;
  }
  .card-front {
    top: 110px;
    background: radial-gradient(circle at 38% 55%, #3a2f31 0%, var(--card-dark) 45%, var(--card-dark-edge) 100%);
    display: flex;
    align-items: center;
    justify-content: center;
  }
  .card-back { top: 480px; background: var(--card-light); }

  .wordmark {
    display: flex;
    align-items: center;
    gap: 14px;
  }
  .wordmark-dot {
    width: 22px; height: 22px;
    border-radius: 50%;
    background: var(--accent);
  }
  .wordmark-name {
    font-weight: 300;
    letter-spacing: 6px;
    text-transform: uppercase;
    color: var(--logo-grey);
  }
  .card-front .wordmark-name { font-size: 50px; color: #d6d6d6; }

  .card-back .wordmark { position: absolute; left: 34px; top: 48px; gap: 10px; }
  .card-back .wordmark-dot { width: 16px; height: 16px; }
  .card-back .wordmark-name { font-size: 34px; letter-spacing: 4px; }

  .holder {
    position: absolute;
    right: 26px; top: 76px;
    text-align: right;
  }
  .holder-name {
    font-size: 14px;
    letter-spacing: 0.5px;
    color: var(--text-grey);
    text-transform: uppercase;
  }
  .holder-role { font-size: 12px; color: var(--accent); margin-top: 2px; }
  .edge-bar-right {
    position: absolute; right: 0; top: 74px;
    width: 4px; height: 36px; background: var(--accent);
  }

  .contact {
    position: absolute;
    left: 34px; top: 172px;
    list-style: none;
  }
  .contact-item {
    display: flex;
    align-items: flex-start;
    gap: 12px;
    font-size: 11px;
    line-height: 14px;
    color: var(--text-mid);
  }
  .contact-item + .contact-item { margin-top: 8px; }
  .contact-address { margin-bottom: 10px; }
  .company { color: var(--accent); text-transform: uppercase; }
  .icon { width: 14px; height: 14px; flex: none; }
  .edge-bar-left {
    position: absolute; left: 0;
    width: 3px; background: var(--accent);
  }
</style>
</head>
<body>

<section class="card card-front" aria-label="Card front">
  <div class="wordmark">
    <span class="wordmark-dot"></span>
    <span class="wordmark-name">Tolvexa</span>
  </div>
</section>

<section class="card card-back" aria-label="Card back">
  <div class="wordmark">
    <span class="wordmark-dot"></span>
    <span class="wordmark-name">Tolvexa</span>
  </div>

  <span class="edge-bar-right"></span>
  <div class="holder">
    <p class="holder-name">Daniel Whitfield</p>
    <p class="holder-role">Executive Director</p>
  </div>

  <span class="edge-bar-left" style="top:170px;height:44px"></span>
  <span class="edge-bar-left" style="top:232px;height:20px"></span>
  <span class="edge-bar-left" style="top:256px;height:18px"></span>

  <ul class="contact">
    <li class="contact-item contact-address">
      <svg class="icon" viewBox="0 0 14 14" aria-hidden="true">
        <circle cx="7" cy="7" r="6.2" fill="none" stroke="var(--accent)" stroke-width="1.3"/>
        <path d="M7 3.2a2.3 2.3 0 0 1 2.3 2.3c0 1.7-2.3 4.3-2.3 4.3S4.7 7.2 4.7 5.5A2.3 2.3 0 0 1 7 3.2z" fill="var(--accent)"/>
        <circle cx="7" cy="5.5" r="0.8" fill="#fff"/>
      </svg>
      <span><span class="company">Tolvexa</span><br>PO Box 218<br>Harbour Park NSW 2188</span>
    </li>
    <li class="contact-item">
      <svg class="icon" viewBox="0 0 14 14" aria-hidden="true">
        <circle cx="7" cy="7" r="6.2" fill="none" stroke="var(--accent)" stroke-width="1.3"/>
        <path d="M4.6 3.8l1.3-.3.8 1.8-.9.7c.4.9 1.1 1.6 2 2l.7-.9 1.8.8-.3 1.3c-2.9.2-5.6-2.5-5.4-5.4z" fill="var(--accent)"/>
      </svg>
      <span>+234. 810. 442</span>
    </li>
    <li class="contact-item">
      <svg class="icon" viewBox="0 0 14 14" aria-hidden="true">
        <circle cx="7" cy="7" r="7" fill="var(--accent)"/>
        <rect x="3.6" y="4.6" width="6.8" height="4.8" fill="#fff"/>
        <path d="M3.6 4.6L7 7.3l3.4-2.7" fill="none" stroke="var(--accent)" stroke-width="0.8"/>
      </svg>
      <span>hello@tolvexa.com.au</span>
    </li>
    <li class="contact-item">
      <svg class="icon" viewBox="0 0 14 14" aria-hidden="true">
        <circle cx="7" cy="7" r="7" fill="var(--accent)"/>
        <circle cx="7" cy="7" r="3.6" fill="none" stroke="#fff" stroke-width="0.9"/>
        <path d="M3.4 7h7.2M7 3.4c-1.6 2-1.6 5.2 0 7.2M7 3.4c1.6 2 1.6 5.2 0 7.2" fill="none" stroke="#fff" stroke-width="0.8"/>
      </svg>
      <span>www.tolvexa.com.au</span>
    </li>
  </ul>
</section>

</body>
</html>
```